Business Card Design

We are a project managment company specializing in Interior fitout
Tarnwick is for Commercial, Domestic, Industial - we provide managment to these industries and see the projects through design to contruction
Would like an area on the back of the card where peoplr can write notes
Thinking laser lines and architectural finishes
Colour theme at the moment is light grey and red although im open to any colour/design scheme

Industry/Entity Type

Business

Contact Information for Business Card

Tarnwick Projects
Brett Lamonte
Managing Director
0491570110
brett@tarnwick-example.com.au

```html
<!DOCTYPE html>
<html lang="en">
<head>
<meta charset="utf-8">
<title>Tarnwick Projects – Business Card</title>
<link rel="stylesheet" href="https://fonts.googleapis.com/css2?family=Montserrat:wght@500;700;800&family=Open+Sans:wght@400;600&display=swap">
<style>
  :root {
    --red: #e41e26;
    --ink: #1d1d1f;
    --grey-text: #555558;
    --card-light: #fbfbfb;
    --card-mid: #e6e6e8;
    --notes-grey: #ececee;
    --tab-dark: #3a3a3d;
    --page: #d9d9dc;
  }
  * { margin: 0; padding: 0; box-sizing: border-box; }
  html, body { width: 1200px; height: 913px; overflow: hidden; }
  body {
    background: var(--page);
    font-family: "Open Sans", Arial, sans-serif;
    display: flex;
    flex-direction: column;
    align-items: center;
    justify-content: center;
    gap: 56px;
  }
  .card {
    position: relative;
    width: 580px;
    height: 332px;
    border-radius: 18px;
    overflow: hidden;
    box-shadow: 0 8px 24px rgba(0,0,0,.18);
  }

  /* Front */
  .card-front {
    background: radial-gradient(ellipse at 50% 40%, var(--card-light) 0%, var(--card-mid) 100%);
  }
  .company-name {
    position: absolute;
    left: 0; right: 0;
    top: 124px;
    text-align: center;
    font-family: "Montserrat", Arial, sans-serif;
    font-weight: 800;
    font-size: 34px;
    letter-spacing: 0.5px;
    color: var(--ink);
    line-height: 1;
  }
  .front-band {
    position: absolute;
    left: 0; right: 0;
    top: 168px;
    height: 24px;
    background: var(--red);
  }
  .front-tagline {
    position: absolute;
    left: 0; right: 0;
    top: 0;
    line-height: 24px;
    text-align: center;
    font-family: "Montserrat", Arial, sans-serif;
    font-weight: 700;
    font-size: 12px;
    letter-spacing: 1.5px;
    text-transform: uppercase;
    color: #fff;
  }

  /* Back */
  .card-back { background: #fff; }
  .phone {
    position: absolute;
    right: 36px;
    top: 38px;
    display: flex;
    align-items: center;
    gap: 8px;
    font-family: "Montserrat", Arial, sans-serif;
    font-weight: 700;
    font-size: 20px;
    color: var(--ink);
  }
  .accent-square {
    position: absolute;
    left: 34px;
    top: 96px;
    width: 70px;
    height: 66px;
    background: var(--red);
  }
  .person-name {
    position: absolute;
    left: 118px;
    top: 70px;
    font-family: "Montserrat", Arial, sans-serif;
    font-weight: 700;
    font-size: 19px;
    color: var(--red);
  }
  .person-title {
    position: absolute;
    left: 118px;
    top: 95px;
    font-size: 13px;
    color: var(--grey-text);
  }
  .laser-line {
    position: absolute;
    left: 104px; right: 0;
    top: 118px;
    height: 2px;
    background: var(--red);
  }
  .email {
    position: absolute;
    left: 118px;
    top: 136px;
    display: flex;
    align-items: center;
    gap: 8px;
    font-size: 13px;
    color: var(--grey-text);
  }
  .notes-area {
    position: absolute;
    left: 104px; right: 0;
    top: 176px; bottom: 0;
    background:
      repeating-linear-gradient(0deg, rgba(0,0,0,.025) 0 1px, transparent 1px 3px),
      var(--notes-grey);
  }
  .side-block {
    position: absolute;
    left: 0;
    top: 228px;
    width: 104px;
    bottom: 0;
    background: var(--red);
  }
  .notes-tab {
    position: absolute;
    left: 104px;
    top: 228px;
    width: 62px;
    height: 22px;
    background: var(--tab-dark);
    color: #fff;
    font-size: 11px;
    line-height: 22px;
    padding-left: 9px;
    clip-path: polygon(0 0, 84% 0, 100% 50%, 84% 100%, 0 100%);
  }
</style>
</head>
<body>

  <section class="card card-front" aria-label="Business card front">
    <div class="company-name">TARNWICK PROJECTS</div>
    <div class="front-band">
      <div class="front-tagline">Fitout Project Management</div>
    </div>
  </section>

  <section class="card card-back" aria-label="Business card back">
    <div class="phone">
      <svg width="16" height="16" viewBox="0 0 16 16" aria-hidden="true">
        <circle cx="8" cy="8" r="7.5" fill="var(--ink)"/>
        <path d="M5.2 4.2l1.3-.3.8 1.9-.9.7c.4.9 1.1 1.6 2 2l.7-.9 1.9.8-.3 1.3c-2.9.3-5.8-2.6-5.5-5.5z" fill="#fff"/>
      </svg>
      <span>0491570110</span>
    </div>
    <div class="accent-square"></div>
    <div class="person-name">Brett Lamonte</div>
    <div class="person-title">Managing Director</div>
    <div class="laser-line"></div>
    <div class="email">
      <svg width="16" height="16" viewBox="0 0 16 16" aria-hidden="true">
        <circle cx="8" cy="8" r="7.5" fill="#6b6b6e"/>
        <rect x="4" y="5.5" width="8" height="5.5" rx=".6" fill="#fff"/>
        <path d="M4.3 5.8L8 8.6l3.7-2.8" stroke="#6b6b6e" stroke-width=".9" fill="none"/>
      </svg>
      <span>brett@tarnwick-example.com.au</span>
    </div>
    <div class="notes-area" aria-label="Space for notes"></div>
    <div class="side-block"></div>
    <div class="notes-tab">notes</div>
  </section>

</body>
</html>
```